Website for a online coaching platform

I would like a website designed with the same content the same as the one below:

https://www.corvel-ashby.com/

New practitioner Marek Tollvander

Target Market(s)

Injured athletes for treatment and medcal professionals for education

Industry/Entity Type

Professional sport and medical education

Coding

Coded - Design and coding required

Number of Pages Required

5+ page

Colors

Designer to choose colors to be used in the design.

Requirements
Must have
• Same amount and format of pages as sample website

```html
<!DOCTYPE html>
<html lang="en">
<head>
<meta charset="utf-8">
<title>TLV Performance – Rehabilitation Specialist</title>
<link href="https://fonts.googleapis.com/css2?family=Inter:wght@400;500;700;800&display=swap" rel="stylesheet">
<style>
:root{
  --black:#000000;
  --nav-bg:#1c1c1c;
  --white:#ffffff;
  --red:#ff0000;
  --band:#d9d9d9;
  --club-navy:#1d2a5c;
  --club-purple:#3d195b;
  --club-red:#c8102e;
}
*{margin:0;padding:0;box-sizing:border-box}
html,body{width:1200px;height:2210px;overflow:hidden;background:var(--black);font-family:'Inter',sans-serif;color:var(--white)}
.page{position:relative;width:1200px;height:2210px}
.site-nav{position:absolute;left:0;top:0;width:1200px;height:86px;background:var(--nav-bg)}
.brand{position:absolute;display:flex;flex-direction:column;justify-content:center;color:var(--white);font-weight:800;line-height:1}
.brand-name{letter-spacing:0.5px}
.brand-sub{font-weight:800;letter-spacing:2px}
.site-nav .brand{left:64px;top:15px;height:56px}
.site-nav .brand-name{font-size:30px}
.site-nav .brand-sub{font-size:10px;margin-top:3px}
.nav-links{position:absolute;left:349px;top:34px;display:flex;gap:26px;font-size:13px;font-weight:700;list-style:none}
.social{position:absolute;display:flex;gap:10px;font-size:12px;font-weight:700;align-items:center}
.site-nav .social{left:1030px;top:34px}
.hero{position:absolute;left:0;top:86px;width:1200px;height:767px;
  background:radial-gradient(ellipse at 45% 45%, #4a4a50 0%, #1a1a1d 40%, #070708 70%),#000;}
.hero-floor{position:absolute;left:0;bottom:0;width:1200px;height:230px;background:linear-gradient(180deg,rgba(90,20,35,0) 0%,#5a1a28 45%,#3a0f1a 100%)}
.hero-photo{position:absolute;inset:0}
.hero-title{position:absolute;right:103px;top:62px;text-align:right;font-size:81px;font-weight:800;line-height:97px;letter-spacing:-0.5px}
.hero-sub{position:absolute;right:103px;top:376px;text-align:right;font-size:29px;font-weight:700;line-height:36px}
.btn-book{position:absolute;left:864px;top:472px;width:233px;height:63px;background:var(--red);color:var(--white);font-size:26px;display:flex;align-items:center;justify-content:center;gap:18px}
.section-title{position:absolute;left:0;width:1200px;text-align:center;font-size:81px;font-weight:500;letter-spacing:-0.5px}
.testimonials-title{top:960px}
.testimonial-photo{position:absolute;left:101px;top:1106px;width:287px;height:431px;background:linear-gradient(180deg,#1e1e22 0%,#2c2a2c 55%,#151515 100%)}
.testimonial-name{position:absolute;left:507px;top:1145px;font-size:51px;font-weight:700}
.testimonial-quote{position:absolute;left:507px;top:1273px;width:580px;font-size:26px;line-height:32.5px}
.clients-title{top:1645px}
.clients-band{position:absolute;left:101px;top:1783px;width:996px;height:188px;background:var(--band);display:flex;align-items:center;justify-content:space-around;padding:0 20px}
.client{display:flex;align-items:center;gap:8px;font-size:17px;font-weight:700;color:var(--club-navy)}
.client-dot{width:22px;height:22px;border-radius:50%}
.site-footer .brand{left:101px;top:2044px;height:95px}
.site-footer .brand-name{font-size:50px}
.site-footer .brand-sub{font-size:16px;margin-top:6px}
.site-footer .social{left:1020px;top:2118px}
</style>
</head>
<body>
<div class="page">
  <header class="site-nav">
    <div class="brand"><span class="brand-name">TLV</span><span class="brand-sub">PERFORMANCE</span></div>
    <ul class="nav-links">
      <li>About TLV</li><li>Rehabilitation Specialist</li><li>Researcher</li><li>Educator</li><li>Events Calendar</li><li>Contact</li>
    </ul>
    <div class="social"><span>Pictora</span><span>Chirper</span></div>
  </header>

  <section class="hero">
    <div class="hero-photo" role="img" aria-label="Athlete flipping a large tyre in a dark gym">
      <div class="hero-floor"></div>
    </div>
    <h1 class="hero-title">Performance<br>Rehabilitation<br>Specialist</h1>
    <p class="hero-sub">Expertise in Rehabilitation, Injury<br>Prevention and Athletic Performance</p>
    <a class="btn-book">Book TLV <span>&gt;</span></a>
  </section>

  <h2 class="section-title testimonials-title">Testimonials</h2>
  <div class="testimonial-photo" role="img" aria-label="Athlete leaping to slam a medicine ball in a gym"></div>
  <h3 class="testimonial-name">Dummy Text</h3>
  <p class="testimonial-quote">Lorem ipsum dolor sit amet, consectetuer adipiscing elit. Aenean commodo ligula eget dolor. Aenean massa. Cum sociis natoque penatibus et magnis dis parturient montes, nascetur ridiculus mus. Donec quam felis, ultricies nec, pellentesque eu, pretium quis, sem. Nulla consequat massa quis enim.</p>

  <h2 class="section-title clients-title">Past Clients</h2>
  <div class="clients-band">
    <div class="client"><span class="client-dot" style="background:var(--club-navy)"></span>Continental Cup</div>
    <div class="client" style="color:var(--club-purple)"><span class="client-dot" style="background:var(--club-purple)"></span>Prime Division</div>
    <div class="client" style="color:var(--club-red)"><span class="client-dot" style="background:var(--club-red)"></span>Northgate United</div>
    <div class="client" style="color:var(--club-red)"><span class="client-dot" style="background:var(--club-red)"></span>Merseyvale FC</div>
    <div class="client" style="color:var(--club-red)"><span class="client-dot" style="background:var(--club-red)"></span>Kingsbridge FC</div>
  </div>

  <footer class="site-footer">
    <div class="brand"><span class="brand-name">TLV</span><span class="brand-sub">PERFORMANCE</span></div>
    <div class="social"><span>Pictora</span><span>Chirper</span></div>
  </footer>
</div>
</body>
</html>
```